Business Brochure Design Project

BRIGHTFERN VENTURE SERVICES
Our company requires a business brochure designed, this design will be printed and emailed to prospective corporate clients to provide an understanding of our businesses services. The written content required in this brochure is attached as a word document.

DESIGN
The design needs to hold your attention and identify the company brand. An A4 portrait format will be used with a white background. Brochure pages will never be viewed side by side as most clients will recieve this as a pdf document attached to an email so considered this in your design. Colour graphics and images will be used to enhance the content and draw people in. To reflect quality, only high resolution images that are clear, sharp and in focus will be used. Please use the CMYK colour model when designing as this brochure will also be printed.

LOOK AND FEEL
The design needs to be savvy, appear uncluttered and have an attitude of a market leader. I want something that stands out in the crowd and effectively markets my businesses brand. It needs to be elegant, modern and have a corporate feel. I want something that has energy, is fresh, innovative, exciting and inviting.

FINISHED PRODUCT
All content in the photo shop design needs to be fully editable including text. Our business has a copy of photo shop CS6, so the finished product must be compatible with this version of software. Each page must contain the text “Copyright © 2013 Brightfern Venture Services. All rights reserved”
Updates

Hi all

I will also be setting up a stationay project soon, if your are interested in being part of it please let me know.

Thanks

                          

I like designs that use a white background with the use of red, black and grey colours within

 

To all designers

Thanks for the great design work; I look forward to working with you all again in the future

 

Regards Marcus Delaney

Industry/Entity Type

Shop

Requirements
Must have
• This design must be professional and of the highest calibre

Please use the CMYK colour model as this is the formatt by printers.

Business contact details must be clearly visible on the cover page
Should not have
• Each part of my business advertising needs to look interesting in its own right. This insures companies are intrigued to find out more about our services, who we are and what we do. Please do not design something that looks identical to my webpage site or Facebook page. Your design needs to adds value to the overall promotional impact of my business.

The design should not be based off a generic design template, it needs to be unique.

```html
<!DOCTYPE html>
<html lang="en">
<head>
<meta charset="utf-8">
<title>Brightfern Venture Services – Business Profile</title>
<link rel="stylesheet" href="https://fonts.googleapis.com/css2?family=Michroma&family=Open+Sans:wght@300;400;600;700;800&display=swap">
<style>
:root{
  --red:#e31b23;
  --red-deep:#c8141b;
  --ink:#1c1c1c;
  --charcoal:#3b3b3d;
  --grey:#5d5d60;
  --mist:#e9e9ea;
  --paper:#ffffff;
  --stage:#d9d9db;
}
*{margin:0;padding:0;box-sizing:border-box}
html,body{width:1200px;height:920px;overflow:hidden}
body{background:var(--stage);font-family:"Open Sans",Arial,sans-serif;color:var(--ink);position:relative}
.page{position:absolute;top:121px;width:485px;height:685px;background:var(--paper);overflow:hidden;box-shadow:0 2px 10px rgba(0,0,0,.25)}
.page--cover{left:91px;background:linear-gradient(90deg,#fff 0,#f1f1f1 6%,#fff 10%,#f4f4f4 18%,#fff 24%,#efefef 33%,#fff 40%,#f3f3f3 52%,#fff 60%,#f0f0f0 70%,#fff 78%,#f4f4f4 88%,#fff 100%)}
.page--inside{left:597px}

/* cover */
.brand-mark{position:absolute;left:82px;top:44px;display:flex;align-items:center;gap:10px}
.brand-mark__square{width:34px;height:34px;background:var(--red)}
.brand-mark__name{font-weight:800;font-size:21px;line-height:1;color:var(--ink)}
.brand-mark__tagline{position:absolute;left:82px;top:86px;font-size:8.5px;font-weight:600;color:var(--ink)}
.cover-title{position:absolute;top:200px;width:100%;text-align:center;font-family:"Michroma",sans-serif;font-size:16.5px;color:var(--charcoal);letter-spacing:.5px}
.cover-subtitle{position:absolute;top:238px;width:100%;text-align:center;font-weight:300;font-size:18px;letter-spacing:3px;color:var(--charcoal)}
.cover-wave{position:absolute;left:0;top:0}
.contact{position:absolute;top:362px;left:90px;width:400px;text-align:center;color:#fff}
.contact__heading{font-weight:300;font-size:14px;letter-spacing:.5px;margin-bottom:14px}
.contact__line{font-size:9.5px;line-height:17.5px;white-space:nowrap}
.contact__label{font-weight:300;color:#ffe3e3}
.cover-promise{position:absolute;top:563px;width:100%;text-align:center;color:#fff;font-weight:700;font-size:19px;line-height:24px}
.copyright{font-size:6.5px;color:#fff}
.page--cover .copyright{position:absolute;top:654px;width:100%;text-align:center}

/* inside */
.intro{position:absolute;left:0;top:0;width:100%;height:120px;background:var(--red);color:#fff;padding:29px 31px 0}
.intro__title{font-weight:300;font-size:12.5px;letter-spacing:.4px;margin-bottom:13px}
.intro__text{font-size:6.7px;line-height:10.5px;text-align:justify}
.section-tab{position:absolute;height:19px;background:linear-gradient(#4a4a4c,#2f2f31);color:#fff;font-weight:300;font-size:9.5px;line-height:19px;padding-left:30px;clip-path:polygon(0 0,100% 0,97% 100%,0 100%);letter-spacing:.2px}
.tick-list{position:absolute;list-style:none;font-size:6.6px;line-height:10.6px;color:var(--ink);z-index:2}
.tick-list li{position:relative;padding-left:11px;white-space:nowrap}
.tick-list li::before{content:"";position:absolute;left:0;top:2px;width:6px;height:6px;border:1px solid #bdbdbd;background:#fff}
.tick-list li::after{content:"";position:absolute;left:2px;top:1px;width:3px;height:6px;border-right:1.6px solid var(--red);border-bottom:1.6px solid var(--red);transform:rotate(40deg)}
.portrait-scene{position:absolute;left:28px;top:455px;width:340px;height:200px;background:linear-gradient(90deg,#2d3038 0,#4a4d55 38%,#d9dbe0 55%,#f2f2f3 100%);clip-path:polygon(0 0,46% 0,46% 42%,100% 42%,100% 100%,0 100%);z-index:1}
.inside-brand{position:absolute;left:378px;top:600px;width:90px;font-weight:800;font-size:10px;line-height:12px;color:var(--ink);text-align:right}
.footer-bar{position:absolute;left:0;top:662px;width:100%;height:23px;background:var(--charcoal)}
.footer-bar__red{position:absolute;left:28px;top:1px;width:240px;height:21px;background:var(--red);clip-path:polygon(0 0,100% 0,96% 100%,0 100%);border-radius:8px 0 0 8px}
.footer-bar .copyright{position:absolute;left:12px;top:6px}
.footer-bar__web{position:absolute;right:18px;top:5px;font-size:8.5px;font-weight:700;color:#fff;letter-spacing:.4px}
</style>
</head>
<body>

<section class="page page--cover" aria-label="Cover page">
  <svg class="cover-wave" width="485" height="685" viewBox="0 0 485 685" aria-hidden="true">
    <path d="M0 425 C40 340 170 300 485 280 L485 685 L0 685 Z" fill="var(--red)"/>
  </svg>
  <div class="brand-mark">
    <span class="brand-mark__square"></span>
    <span class="brand-mark__name">BRIGHTFERN VENTURE SERVICES</span>
  </div>
  <p class="brand-mark__tagline">Providing Effective Project Controls and Management Solutions</p>

  <h1 class="cover-title">BRIGHTFERN VENTURE SERVICES</h1>
  <p class="cover-subtitle">BUSINESS PROFILE</p>

  <div class="contact">
    <h2 class="contact__heading">CONTRACT DETAILS</h2>
    <p class="contact__line"><span class="contact__label">DIRECTOR:</span> MARCUS DELANEY</p>
    <p class="contact__line"><span class="contact__label">MOBILE:</span> +61 0400 555 018</p>
    <p class="contact__line"><span class="contact__label">WEBSITE:</span> www.brightfernventures.com.au</p>
    <p class="contact__line"><span class="contact__label">EMAIL:</span> marcus@brightfernventures.com.au</p>
    <p class="contact__line"><span class="contact__label">LINKDEN:</span> www.example-network.com/in/mdelaneybrightfern</p>
    <p class="contact__line"><span class="contact__label">FACE BOOK:</span> www.example-social.com/BrightfernVentureServices</p>
  </div>

  <p class="cover-promise">Providing effective project controls<br>and management solutions within<br>australia and overseas</p>
  <p class="copyright">Copyright © 2013 Brightfern Venture Services. All rights reserved</p>
</section>

<section class="page page--inside" aria-label="Services page">
  <header class="intro">
    <h2 class="intro__title">BRIGHTFERN VENTURE SERVICES</h2>
    <p class="intro__text">Brightfern Venture Services provides effective project controls and management solutions for construction projects in Australia and Overseas. We provide services to both large multinational companies and smaller privately owned businesses. Our knowledge and expertise assist clients to effectively plan and manage their construction projects or project portfolios. Our focus is to provide your business with the tools, solutions and strategies necessary to deliver projects on time and within budget. We provide short or long term support, depending on your needs.</p>
  </header>

  <h3 class="section-tab" style="left:0;top:150px;width:194px">SUPPORTING CLIENTS IN</h3>
  <ul class="tick-list" style="left:31px;top:176px">
    <li>OIL &amp; Gas</li><li>Coal</li><li>Building and Construction</li><li>Civil</li><li>Petrochemical</li>
  </ul>
  <ul class="tick-list" style="left:148px;top:176px">
    <li>Iron Ore</li><li>New Industries</li><li>Rail</li><li>Manufacturing</li><li>Telecommunications</li>
  </ul>

  <h3 class="section-tab" style="left:3px;top:255px;width:192px">BENEFITS OF USING OUR SERVICES</h3>
  <ul class="tick-list" style="left:31px;top:281px">
    <li>Identify project risks</li><li>Stream line processes</li><li>Improving project visibility</li><li>Influencing project outcomes</li><li>Plan &amp; control budgets</li><li>Providing strategic planning advice</li><li>Creating collaborative working environments</li><li>Supporting projects in Australia and Overseas</li><li>Monitor and report progress</li><li>Issues addressed &amp; resolved quickly</li><li>Improve productivity and efficiency</li><li>Providing guidance, support and advice</li><li>Delivering successful project outcomes</li><li>Implement business process improvements</li><li>Innovative cost effective tools and solutions</li><li>Coordinating, equipment, manpower and resources</li>
  </ul>

  <h3 class="section-tab" style="left:252px;top:148px;width:204px">BUSINESS VALUE PROVIDED</h3>
  <ul class="tick-list" style="left:272px;top:174px">
    <li>Embrace and drive change</li><li>Exceed client's expectations</li><li>Independent objective view point</li><li>Help businesses develop and evolve</li><li>Deliver consistent lasting improvements</li><li>Provide quality products and services</li><li>Give clients perspective and expert advice</li><li>Develop and nurture business relationships</li><li>Supply specialist skills, knowledge and expertise</li><li>Assist clients to adapt to changing market conditions</li>
  </ul>

  <h3 class="section-tab" style="left:252px;top:302px;width:204px">SUMMARY OF SERVICES PROVIDED</h3>
  <ul class="tick-list" style="left:282px;top:328px">
    <li>Governance &amp; assurance</li><li>Tender preparation and reviews</li><li>Project planning and scheduling</li><li>Business process improvement</li><li>Project and construction management</li><li>Programme and portfolio management</li><li>Independent reviews and risk analysis</li><li>Project support services</li><li>Software selection &amp; integration</li><li>Corporate and project reporting</li><li>Forecasting and data analysis</li><li>Earned value, monitoring and evaluation</li><li>Manpower &amp; equipment optimisation</li><li>Cost control and change management</li><li>Introduce systems, standards and procedures</li><li>Develop project management frameworks</li>
  </ul>

  <div class="portrait-scene" role="img" aria-label="Photograph of a businessman in a suit with arms crossed, in front of an empty boardroom table"></div>
  <p class="inside-brand">BRIGHTFERN VENTURE SERVICES</p>

  <footer class="footer-bar">
    <div class="footer-bar__red"><p class="copyright">Copyright © 2013 Brightfern Venture Services. All rights reserved</p></div>
    <p class="footer-bar__web">www.brightfernventures.com.au</p>
  </footer>
</section>

</body>
</html>
```